Copper Ridge Stewardship Summit needs a marketing flyer

We need a full page graphic for our upcoming Forum that can also be converted into a website "header" for social media, etc.: "Copper Ridge Stewardship Summit - Making Impact Through the Built Environment"

INTRODUCTION:
During the first week of August 2022, Q-VarDT is presenting the Copper Ridge Stewardship Summit - Making Impact Through the Built Environment.

One of the most exciting aspects of this conference will be the bringing together of multiple organizations including for-profits and nonprofits, K-12’s and higher education, cities and counties and other governmental agencies, as well as architects, engineers, and contractors to collaboratively present and discuss issues and ideas related to sustainability, with a Texas focus.

This event will be a catalyst for public and private project owners to holistically gather information and momentum as we bring the resources and vision needed to achieve the goal of zero carbon emissions from the built environment by 2040, and address water, green space and the natural environment, transportation, equity, and funding, among other topics.

```html
<!DOCTYPE html>
<html lang="en">
<head>
<meta charset="utf-8">
<title>Copper Ridge Stewardship Summit – Flyer</title>
<link rel="stylesheet" href="https://fonts.googleapis.com/css2?family=Montserrat:wght@300;400;500;700;800&family=Ubuntu:wght@500&display=swap">
<style>
  :root{
    --backdrop:#e6e2dc;
    --paper:#ffffff;
    --navy:#1b3a93;
    --green:#5b8a13;
    --pill:#5a8c12;
    --ink:#222222;
    --panel-top:#ececec;
    --panel-bottom:#f7f7f7;
    --photo-dark:#141a12;
    --photo-mid:#2e3d22;
    --photo-light:#4f6a33;
  }
  *{box-sizing:border-box;margin:0;padding:0}
  html,body{width:1200px;height:1200px;overflow:hidden;background:var(--backdrop)}
  body{font-family:"Montserrat",sans-serif;color:var(--ink)}

  .flyer{
    position:absolute;left:160px;top:30px;width:880px;height:1140px;
    background:var(--paper);overflow:hidden;
    box-shadow:0 6px 18px rgba(0,0,0,.18);
  }

  .hero{position:absolute;left:0;top:0;width:880px;height:509px}
  .hero-photo{
    position:absolute;inset:0;
    background:
      radial-gradient(ellipse 55% 45% at 50% 40%, var(--photo-light) 0%, transparent 70%),
      linear-gradient(180deg, var(--photo-mid) 0%, var(--photo-dark) 65%, #2a2018 100%);
  }
  .hero-cap{position:absolute;left:0;top:0}

  .brand{
    position:absolute;top:30px;left:0;width:880px;
    display:flex;justify-content:center;align-items:center;gap:18px;
  }
  .brand-dot{width:76px;height:76px;border-radius:50%;background:var(--navy)}
  .brand-name{font-weight:500;font-size:40px;color:#333;letter-spacing:.5px}

  .hero-title{
    position:absolute;left:0;width:880px;text-align:center;color:#fff;
    text-transform:uppercase;line-height:1;
  }
  .hero-title .line-1{display:block;font-weight:800;font-size:64px;position:absolute;top:-300px;width:880px}
  .title-1{top:300px;font-weight:800;font-size:64px;letter-spacing:1px}
  .title-2{top:368px;font-weight:500;font-size:54px;letter-spacing:1px}

  .tagline-pill{
    position:absolute;left:75px;top:429px;width:730px;height:36px;
    border-radius:18px;background:var(--pill);
    font-family:"Ubuntu",sans-serif;font-weight:500;font-size:26px;color:#fff;
    display:flex;align-items:center;justify-content:center;letter-spacing:.3px;
  }

  .intro{position:absolute;left:0;top:536px;width:880px;text-align:center}
  .intro-lead{font-weight:500;font-size:26px;line-height:43px}
  .intro-lead strong{font-weight:800;color:var(--navy)}
  .intro-lead b{font-weight:800;color:var(--ink)}
  .intro-title{font-weight:800;font-size:33px;color:var(--navy);line-height:38px;text-transform:uppercase}
  .intro-sub{font-family:"Ubuntu",sans-serif;font-weight:500;font-size:28px;color:var(--green);line-height:34px}

  .details{
    position:absolute;left:50px;top:710px;width:780px;height:299px;
    border-radius:28px;
    background:linear-gradient(180deg,var(--panel-top),var(--panel-bottom));
    padding:18px 32px 0;
    box-shadow:0 10px 14px -10px rgba(0,0,0,.18);
  }
  .details p{font-weight:300;font-size:17.5px;line-height:24.5px;text-align:justify;color:#1f1f1f}
  .details p + p{margin-top:24.5px}
  .details strong{font-weight:700;color:#111}

  .footer-band{
    position:absolute;left:0;top:1069px;width:880px;height:71px;background:var(--navy);
    display:flex;align-items:center;justify-content:center;
    color:#fff;font-weight:500;font-size:28px;letter-spacing:3px;
  }
</style>
</head>
<body>
  <main class="flyer">
    <section class="hero">
      <div class="hero-photo" role="img" aria-label="Photo of a hand holding seedlings growing from soil and stacked coins, dark green background"></div>
      <svg class="hero-cap" width="880" height="140" viewBox="0 0 880 140" aria-hidden="true">
        <path d="M0 0 H880 V36 H710 C645 36 640 124 570 124 H330 C255 124 250 36 185 36 H0 Z" fill="#f3f3f3"/>
      </svg>
      <div class="brand">
        <span class="brand-dot"></span>
        <span class="brand-name">Q-VarDT</span>
      </div>
      <h1>
        <span class="hero-title title-1">Copper Ridge</span>
        <span class="hero-title title-2">Stewardship Summit</span>
      </h1>
      <div class="tagline-pill">Making Impact Through the Built Environment</div>
    </section>

    <section class="intro">
      <p class="intro-lead">During the first week of <strong>AUGUST 2022</strong>,</p>
      <p class="intro-lead"><b>Q-VarDT</b> is presenting the</p>
      <h2 class="intro-title">Copper Ridge Stewardship Summit</h2>
      <p class="intro-sub">Making Impact Through the Built Environment.</p>
    </section>

    <section class="details">
      <p>One of the most exciting aspects of this conference will be the bringing together of <strong>multiple organizations</strong> including for-profits and nonprofits, K-12’s and higher education, cities and counties and other governmental agencies, as well as architects, engineers, and contractors to collaboratively <strong>present and discuss issues and ideas related to sustainability</strong>, with a Texas focus.</p>
      <p>This event will be a catalyst for public and private project owners to holistically gather information and momentum as we bring the resources and vision needed to achieve <strong>the goal of zero carbon emissions from the built environment by 2040</strong>, and address water, green space and the natural environment, transportation, equity, and funding, among other topics.</p>
    </section>

    <footer class="footer-band">www.qvardt.com</footer>
  </main>
</body>
</html>
```